Music Quizz Application

Hello,

I want a new design for my Blind test (music quizz) application on Velphon. You will find attached the images I want to replace. I need something with the same element (menu / song title) but with a different look!

Same, new icon, you have carte blanche to this one.

I am looking for something fresh…. I'm looking for something with a real artistic choice, contrast, colours, etc.

As a marketing screenshot, I want something classic, you'll find an example attached, feel free to innovate.

To sum-up :

- One new view for my App
- One new icon
- One marketing screenshot

screen resolution :
640×960
icon resolution :
1024x1024

Target Market(s)

15-30 years

Industry/Entity Type

Marketing

```html
<!DOCTYPE html>
<html lang="en">
<head>
<meta charset="utf-8">
<title>Music Quizz – Choose a Universe</title>
<link href="https://fonts.googleapis.com/css2?family=Arimo:wght@400;700&display=swap" rel="stylesheet">
<style>
:root{
  --status-bg:#4b5154;
  --status-text:#f2f2f2;
  --title-ink:#1c3a48;
  --tab-home:#6fcfd0;
  --tab-rankings:#d1d9d2;
  --tab-community:#a2dcc2;
  --tab-ink:#1f3f4c;
  --tab-rule:#1f4654;
  --band:#6dcdce;
  --band-text:#ffffff;
  --row-a:#2f7e97;
  --row-b:#3690aa;
  --row-text:#d7e5e8;
  --box:#2a6f87;
  --accent:#f58a1f;
  --footer:#276b84;
  --scroll-track:#2c6f86;
  --scroll-thumb:#d8dedd;
}
*{box-sizing:border-box;margin:0;padding:0}
html,body{width:800px;height:1200px;overflow:hidden;background:var(--status-bg)}
body{font-family:"Arimo",Arial,sans-serif;position:relative}
.screen{position:relative;width:800px;height:1200px;overflow:hidden}

.status-bar{position:absolute;left:0;top:0;width:800px;height:50px;background:var(--status-bg);color:var(--status-text);font-weight:700;font-size:28px}
.status-bar .carrier{position:absolute;left:10px;top:9px;display:flex;align-items:flex-end;gap:8px}
.status-bar .time{position:absolute;left:0;width:800px;top:9px;text-align:center}
.status-bar .battery{position:absolute;right:12px;top:12px}

.app-header{position:absolute;left:0;top:50px;width:800px;height:110px}
.app-header .backdrop{position:absolute;inset:0;background:linear-gradient(90deg,#8fd3d0 0%,#4fb5b6 25%,#9ee0d8 50%,#5cc0bd 75%,#8fd6cf 100%)}
.app-title{position:absolute;left:0;width:800px;top:18px;text-align:center;font-size:60px;font-weight:700;color:var(--title-ink);letter-spacing:-0.5px}
.menu-button{position:absolute;left:26px;top:38px}
.settings-button{position:absolute;right:12px;top:20px}

.tabs{position:absolute;left:0;top:160px;width:800px;height:111px;display:flex;border-top:2px solid var(--tab-rule)}
.tab{flex:1;display:flex;align-items:center;justify-content:center;font-size:27px;font-weight:700;color:var(--tab-ink);letter-spacing:0.3px}
.tab + .tab{border-left:2px solid var(--tab-rule)}
.tab-home{background:var(--tab-home)}
.tab-rankings{background:var(--tab-rankings)}
.tab-community{background:var(--tab-community)}

.prompt{position:absolute;left:0;top:271px;width:787px;height:61px;background:var(--band);color:var(--band-text);font-size:20px;font-weight:700;display:flex;align-items:center;justify-content:center}

.universe-list{position:absolute;left:0;top:332px;width:787px;height:758px;overflow:hidden;list-style:none}
.universe{height:66px;display:flex;align-items:center;padding-left:78px;position:relative;color:var(--row-text);font-size:27px;font-weight:700}
.universe:nth-child(odd){background:var(--row-a)}
.universe:nth-child(even){background:var(--row-b)}
.universe .count{margin-left:22px}
.checkbox{position:absolute;left:697px;top:13px;width:42px;height:42px;background:var(--box)}
.checkbox svg{position:absolute;left:-3px;top:-12px}

.scrollbar{position:absolute;left:787px;top:271px;width:13px;height:819px;background:var(--scroll-track)}
.scrollbar .thumb{position:absolute;left:0;top:68px;width:13px;height:462px;background:var(--scroll-thumb)}
.scrollbar .top{position:absolute;left:0;top:0;width:13px;height:68px;background:var(--band)}

.join-bar{position:absolute;left:0;top:1090px;width:800px;height:110px;background:var(--footer);color:var(--accent);font-size:36px;font-weight:700;display:flex;align-items:center;justify-content:center}
</style>
</head>
<body>
<main class="screen">
  <div class="status-bar">
    <div class="carrier">
      <svg width="44" height="22" viewBox="0 0 44 22" aria-hidden="true">
        <rect x="0" y="16" width="6" height="6" fill="#f2f2f2"/>
        <rect x="9" y="12" width="6" height="10" fill="#f2f2f2"/>
        <rect x="18" y="8" width="6" height="14" fill="#f2f2f2"/>
        <rect x="27" y="4" width="6" height="18" fill="#f2f2f2"/>
        <rect x="36" y="0" width="6" height="22" fill="#f2f2f2"/>
      </svg>
      <span>VOXEL</span>
    </div>
    <div class="time">2:34</div>
    <svg class="battery" width="52" height="26" viewBox="0 0 52 26" aria-hidden="true">
      <rect x="1.5" y="1.5" width="44" height="23" rx="3" fill="none" stroke="#f2f2f2" stroke-width="3"/>
      <rect x="6" y="6" width="35" height="14" fill="#f2f2f2"/>
      <rect x="47" y="8" width="4" height="10" fill="#f2f2f2"/>
    </svg>
  </div>

  <header class="app-header">
    <div class="backdrop" role="img" aria-label="Soft teal mosaic background texture"></div>
    <svg class="menu-button" width="34" height="32" viewBox="0 0 34 32" aria-label="Menu">
      <g fill="#1c3a48">
        <rect x="0" y="2" width="6" height="6"/><rect x="10" y="2" width="24" height="6"/>
        <rect x="0" y="13" width="6" height="6"/><rect x="10" y="13" width="24" height="6"/>
        <rect x="0" y="24" width="6" height="6"/><rect x="10" y="24" width="24" height="6"/>
      </g>
    </svg>
    <h1 class="app-title">Music Quizz</h1>
    <svg class="settings-button" width="72" height="76" viewBox="0 0 72 76" aria-label="Settings">
      <polygon points="36,3 68,21 68,55 36,73 4,55 4,21" fill="none" stroke="#1c3a48" stroke-width="5"/>
      <g transform="translate(36 38)" fill="#1c3a48">
        <circle r="9"/>
        <g>
          <rect x="-3" y="-14" width="6" height="28"/>
          <rect x="-3" y="-14" width="6" height="28" transform="rotate(45)"/>
          <rect x="-3" y="-14" width="6" height="28" transform="rotate(90)"/>
          <rect x="-3" y="-14" width="6" height="28" transform="rotate(135)"/>
        </g>
        <circle r="4" fill="#7fcac6"/>
      </g>
    </svg>
  </header>

  <nav class="tabs">
    <div class="tab tab-home">HOME</div>
    <div class="tab tab-rankings">RANKINGS</div>
    <div class="tab tab-community">COMMUNITY</div>
  </nav>

  <p class="prompt">CHOOSE A UNIVERSE TO JOIN THE GAME</p>

  <ul class="universe-list">
    <li class="universe">HITS<span class="count">( 39 people )</span>
      <span class="checkbox"><svg width="50" height="50" viewBox="0 0 50 50" aria-label="Selected"><polyline points="6,26 18,40 42,4" fill="none" stroke="var(--accent)" stroke-width="6" stroke-linecap="round" stroke-linejoin="round"/></svg></span></li>
    <li class="universe">POP<span class="count">( 39 people )</span><span class="checkbox"></span></li>
    <li class="universe">POLISH &amp; WORLD HITS<span class="count" style="margin-left:14px">( 39 people )</span><span class="checkbox"></span></li>
    <li class="universe">NEW WAVE<span class="count">( 39 people )</span><span class="checkbox"></span></li>
    <li class="universe">R&amp;B<span class="count">( 39 people )</span><span class="checkbox"></span></li>
    <li class="universe">HARD,METAL<span class="count">( 39 people )</span><span class="checkbox"></span></li>
    <li class="universe">90’s<span class="count" style="margin-left:32px">( 39 people )</span><span class="checkbox"></span></li>
    <li class="universe">INDIE ROCK<span class="count">( 39 people )</span><span class="checkbox"></span></li>
    <li class="universe">RAP &amp; HIPHOP<span class="count" style="margin-left:14px">( 39 people )</span><span class="checkbox"></span></li>
    <li class="universe">DANCE ,HOUSE ,ELECTRO<span class="count">( 39 people )</span><span class="checkbox"></span></li>
    <li class="universe">ALL GENRES<span class="count">( 39 people )</span><span class="checkbox"></span></li>
    <li class="universe">OLD HITS<span class="count" style="margin-left:12px">( 39 people )</span><span class="checkbox"></span></li>
  </ul>

  <div class="scrollbar" aria-hidden="true"><div class="top"></div><div class="thumb"></div></div>

  <div class="join-bar">JOIN THE GAME</div>
</main>
</body>
</html>
```